4x6 -ish post card to let the neighborhood know where here.

Hi All, I opened a high end wine & spirits shop and am looking to get out some sort of a 4x6 postcard a flyer to let people know where in the area. Looking for something clean cut that can maybe incorporate a few pictures from our store on along the top and our logo. Ideally a white-ish background.

```html
<!DOCTYPE html>
<html lang="en">
<head>
<meta charset="utf-8">
<title>Stonebrook Wine &amp; Spirits Postcard</title>
<link href="https://fonts.googleapis.com/css2?family=Cinzel:wght@600;700&family=Playfair+Display:wght@700&family=Open+Sans:wght@400;600&display=swap" rel="stylesheet">
<style>
:root{
  --stage:#d9d9d9;
  --card:#ffffff;
  --gold:#b8862f;
  --brown:#8a5a1f;
  --ink:#3a3a3a;
  --muted:#777777;
  --shelf-dark:#2d2a2c;
  --shelf-mid:#5b4a46;
  --shelf-light:#b9a79a;
  --fridge:#3f5e78;
}
*{box-sizing:border-box;margin:0;padding:0}
html,body{width:1200px;height:2212px;overflow:hidden}
body{background:var(--stage);font-family:"Open Sans",sans-serif;position:relative}
.postcard{position:absolute;left:60px;width:1080px;height:720px;background:var(--card);overflow:hidden;box-shadow:0 6px 18px rgba(0,0,0,.18)}
.postcard--front{top:360px}
.postcard--back{top:1180px}
.brand{position:absolute;display:flex;align-items:center;gap:14px}
.brand__mark{width:18px;height:18px;background:var(--gold);flex:none}
.brand__name{font-family:"Cinzel",serif;font-weight:700;color:var(--brown);line-height:1.05;white-space:nowrap}
.front__brand{left:56px;top:56px}
.front__brand .brand__name{font-size:50px}
.intro{position:absolute;left:56px;top:230px;width:440px}
.intro__title{font-family:"Playfair Display",serif;font-weight:700;color:var(--brown);font-size:36px;line-height:1.15}
.intro__text{margin-top:12px;color:var(--ink);font-size:23px;line-height:1.35}
.photo-row{position:absolute;left:56px;top:470px;display:flex;gap:16px}
.photo{display:block}
.photo--small{width:214px;height:130px;background:linear-gradient(135deg,var(--fridge),#9fb4c4 55%,var(--shelf-dark))}
.photo--small.alt{background:linear-gradient(135deg,#cfd6da,var(--fridge) 60%,#222)}
.photo--store{position:absolute;right:0;top:0;width:520px;height:720px;background:linear-gradient(160deg,#e8ddd0 0%,var(--shelf-light) 22%,var(--shelf-mid) 55%,var(--shelf-dark) 100%)}
.gold-bar{position:absolute;left:548px;top:0;width:12px;height:720px;background:var(--gold)}
.contact{position:absolute;display:flex;align-items:center;gap:22px;font-size:17px;color:var(--muted)}
.contact__item{display:flex;align-items:center;gap:7px}
.contact svg{width:18px;height:18px}
.front__contact{left:56px;top:650px}
.back__art{position:absolute;left:0;top:0}
.back__brand{left:470px;top:225px}
.back__brand .brand__name{font-size:48px}
.stamp{position:absolute;right:50px;top:40px;width:130px;height:160px;border:2px solid #b5b5b5}
.back__contact{right:50px;top:660px}
</style>
</head>
<body>

<section class="postcard postcard--front">
  <div class="brand front__brand">
    <span class="brand__mark"></span>
    <span class="brand__name">Stonebrook<br>Wine &amp; Spirits</span>
  </div>
  <div class="intro">
    <h2 class="intro__title">Stonebrook<br>Wine &amp; Spirits,</h2>
    <p class="intro__text">Your local package store to satisfy all of your tastes without breaking the bank or making it complex.</p>
  </div>
  <div class="photo-row">
    <span class="photo photo--small" role="img" aria-label="Store photo: chilled drinks coolers"></span>
    <span class="photo photo--small alt" role="img" aria-label="Store photo: glass-door fridge display"></span>
  </div>
  <div class="contact front__contact">
    <span class="contact__item"><svg viewBox="0 0 24 24"><path fill="var(--gold)" d="M6.6 10.8a15 15 0 0 0 6.6 6.6l2.2-2.2a1 1 0 0 1 1-.25 11.4 11.4 0 0 0 3.6.6 1 1 0 0 1 1 1V20a1 1 0 0 1-1 1A17 17 0 0 1 3 4a1 1 0 0 1 1-1h3.5a1 1 0 0 1 1 1c0 1.25.2 2.45.6 3.6a1 1 0 0 1-.25 1z"/></svg>+1 555-014-2290</span>
    <span class="contact__item"><svg viewBox="0 0 24 24"><circle cx="12" cy="12" r="9" fill="none" stroke="var(--gold)" stroke-width="2"/><path d="M3 12h18M12 3c3 3 3 15 0 18M12 3c-3 3-3 15 0 18" fill="none" stroke="var(--gold)" stroke-width="1.6"/></svg>STONEBROOKWINE.COM</span>
  </div>
  <span class="gold-bar"></span>
  <span class="photo photo--store" role="img" aria-label="Store photo: interior with wine racks and bottle shelves"></span>
</section>

<section class="postcard postcard--back">
  <svg class="back__art" width="1080" height="720" viewBox="0 0 1080 720">
    <g role="img" aria-label="Collage of store photos: wine shelves and bottle displays">
      <polygon points="0,0 300,0 0,300" fill="#4d3f3c"/>
      <polygon points="310,0 330,0 330,210 20,520 0,520 0,310" fill="#6d5a52"/>
      <polygon points="0,530 20,530 250,300 250,720 0,720" fill="#2f2a2c"/>
      <polygon points="260,300 340,220 340,720 260,720" fill="#8c7a6e"/>
    </g>
    <polygon points="400,345 525,470 400,595 275,470" fill="var(--gold)"/>
  </svg>
  <div class="brand back__brand">
    <span class="brand__mark"></span>
    <span class="brand__name">Stonebrook<br>Wine &amp; Spirits</span>
  </div>
  <div class="stamp"></div>
  <div class="contact back__contact">
    <span class="contact__item"><svg viewBox="0 0 24 24"><path fill="var(--gold)" d="M6.6 10.8a15 15 0 0 0 6.6 6.6l2.2-2.2a1 1 0 0 1 1-.25 11.4 11.4 0 0 0 3.6.6 1 1 0 0 1 1 1V20a1 1 0 0 1-1 1A17 17 0 0 1 3 4a1 1 0 0 1 1-1h3.5a1 1 0 0 1 1 1c0 1.25.2 2.45.6 3.6a1 1 0 0 1-.25 1z"/></svg>+1 555-014-2290</span>
    <span class="contact__item"><svg viewBox="0 0 24 24"><circle cx="12" cy="12" r="9" fill="none" stroke="var(--gold)" stroke-width="2"/><path d="M3 12h18M12 3c3 3 3 15 0 18M12 3c-3 3-3 15 0 18" fill="none" stroke="var(--gold)" stroke-width="1.6"/></svg>STONEBROOKWINE.COM</span>
  </div>
</section>

</body>
</html>
```